Drone Brochure: NDVI For Golf Courses

I need a flier / brochure (probably a tri fold) that speaks to Golf Course Superintendents about the benefits of Drone NDVI imaging. We are a drone flight company service Alberta, We can do aerial images of the course but specialize mostly in NDVI and mapping. We are pushing to sell the NDVI subscription where we would fly 1 per week or 1 per every 2 weeks.

Our company color is blue (RGB 82,150,208 / WEB #5296d0), Golf course stuff seems to incorporate alot of green. Our sample is an example of what could work, with the arrows between areas being a golf cart path?

I use indesign, illustrator and photoshop cs6, and would be looking for compatible files with included font install files if you use a font we don't have. We can try and provide any info you need and pictures you need if you cant find suitable / awesome ones.

Target Market(s)

Golf Course Management

Industry/Entity Type

Golf Course

Font styles to use
Sans Serif

Colors
33a6d7
acd036
0292cd
abd036

Requirements
Must have
• Compelling design, some info general info about NDVI, and specifics about golf course turf health. We can supply some stats and features / benefits list when needed.
• Please ask for any additional info or resources.
• colors are negotiable
Nice to have
• As in the example, thought about the brochure walking the reader through the process, and the links from pictures as a golf cart path. lots of green grass to show healty turf. pictures have a nice border? needs to speak to management of golf courses
Should not have
• cheesy graphics,
• The purple and green pictures that are {same} horizontal should not use the full image, crop down as they are a supplier image we can use but not as the whole thing, the rest are all.

```html
<!DOCTYPE html>
<html lang="en">
<head>
<meta charset="utf-8">
<title>Vantage Aerial Turf – Tri-fold Brochure</title>
<link href="https://fonts.googleapis.com/css2?family=Ubuntu:wght@500;700&family=Montserrat:wght@400;500;600&display=swap" rel="stylesheet">
<style>
:root{
  --backdrop:#a9c9e2;
  --ink:#1c1c1c;
  --paper:#f4f5f6;
  --brand-blue:#5296d0;
  --brand-dark:#3a3d42;
  --turf-dark:#3f5a23;
  --turf-mid:#7b8f35;
  --turf-light:#b9b46a;
  --sky:#6f9fd3;
}
*{box-sizing:border-box;margin:0;padding:0}
html,body{width:1200px;height:900px;overflow:hidden}
body{background:var(--backdrop);font-family:"Montserrat",Arial,sans-serif;color:var(--ink)}
.brochure{position:absolute;left:30px;top:30px;width:1140px;height:840px;display:flex;box-shadow:0 10px 30px rgba(0,0,0,.25)}
.panel{position:relative;width:380px;height:840px;overflow:hidden}
.heading{font-family:"Ubuntu",Arial,sans-serif;font-weight:700;font-size:23px;color:var(--ink);display:inline-block;padding-bottom:6px;border-bottom:4px solid var(--ink);border-radius:0 0 2px 2px}
.copy{font-size:12.3px;line-height:15px;text-align:justify}
.copy + .copy{margin-top:15px}

/* Left panel */
.panel--services{background:var(--paper)}
.services__top{position:absolute;left:0;top:0;width:380px;height:500px;background:linear-gradient(#f4f5f6 78%,rgba(244,245,246,0))}
.services__title{position:absolute;left:30px;top:26px}
.turf-maps{position:absolute;left:8px;top:80px;width:364px;height:225px;display:flex;gap:2px}
.turf-map{flex:1;height:100%}
.turf-map--true{background:radial-gradient(ellipse 38% 48% at 50% 50%,#9aa35a,#6f8a3e 70%,#3e5b2a)}
.turf-map--ndvi{background:radial-gradient(ellipse 38% 48% at 50% 50%,#c4d47a,#5fa83f 70%,#1f6e2a)}
.services__intro{position:absolute;left:30px;top:318px;width:324px}
.services__photo{position:absolute;left:0;top:440px;width:380px;height:400px;background:linear-gradient(#d9d6cc 0%,#8f7a4f 35%,#9a8a3a 60%,#6e7a2c 100%)}
.services__features{position:absolute;left:28px;top:505px;width:326px;color:#fff}
.services__features .heading{color:#fff;border-color:#fff;font-weight:500;font-size:22px;margin-bottom:14px}

/* Middle panel */
.panel--about{background:var(--paper)}
.about__photo{position:absolute;left:0;bottom:0;width:380px;height:420px;background:linear-gradient(rgba(244,245,246,1) 0%,rgba(228,226,205,.9) 50%,#cfc98d 100%)}
.about__body{position:absolute;left:28px;top:36px;width:326px}
.about__body .heading{font-size:22px;margin-bottom:14px}
.contact{position:absolute;left:28px;top:522px;width:326px}
.contact .heading{font-size:22px;margin-bottom:20px}
.contact__list{display:grid;grid-template-columns:70px 14px auto;font-size:13.5px;line-height:18px;margin-left:6px}
.contact__list dt{text-align:right}
.contact__list dd{margin:0}
.brand-mark{position:absolute;left:0;width:380px;top:700px;text-align:center}
.brand-mark__name{font-family:"Ubuntu",Arial,sans-serif;font-weight:700;font-size:22px;color:var(--brand-blue);display:inline-flex;align-items:center;gap:10px}
.brand-mark__dot{width:14px;height:14px;border-radius:50%;background:var(--brand-blue)}

/* Right panel */
.panel--cover{background:linear-gradient(#4f7fc4 0%,#8aa6b8 22%,#b4b25a 45%,#6f8a2c 70%,#3f5a1e 100%)}
.cover__seal{position:absolute;left:28px;top:120px;width:262px;height:262px;border-radius:50%;background:#f2f3f4;display:flex;align-items:center;justify-content:center;box-shadow:0 4px 14px rgba(0,0,0,.25)}
.cover__name{font-family:"Ubuntu",Arial,sans-serif;font-weight:700;font-size:26px;line-height:32px;color:var(--brand-dark);text-align:center}
</style>
</head>
<body>
<main class="brochure">

  <section class="panel panel--services">
    <div class="services__photo" role="img" aria-label="Soft-focus photo of a golf course fairway in warm light"></div>
    <div class="services__top"></div>
    <h2 class="heading services__title">UAV Turf Health Services</h2>
    <div class="turf-maps">
      <div class="turf-map turf-map--true" role="img" aria-label="Aerial photo of a golf green"></div>
      <div class="turf-map turf-map--ndvi" role="img" aria-label="NDVI map of the same green with a stressed area circled"></div>
    </div>
    <p class="copy services__intro">Lorem ipsum dolor sit amet, consectetur adipiscing elit. Sed dignissim sollicitudin lectus, quis feugiat libero maximus eget. Fusce tincidunt fermentum ligula sed tincidunt. Orci varius natoque penatibus et magnis dis parturient montes, nascetur ridiculus mus. Pellentesque dapibus tellus id iaculis malesuada. Etiam tincidunt mi at tortor vulputate ullamcorper. Proin porta magna ac risus aliquam, vitae posuere nibh feugiat. Aliquam erat volutpat. Aliquam luctus sodales orci.</p>
    <div class="services__features">
      <h2 class="heading">Features and Benefits</h2>
      <p class="copy">Lorem ipsum dolor sit amet, consectetur adipiscing elit. Sed dignissim sollicitudin lectus, quis feugiat libero maximus eget. Fusce tincidunt fermentum ligula sed tincidunt. Orci varius natoque penatibus et magnis dis parturient montes, nascetur ridiculus mus. Pellentesque dapibus tellus id iaculis malesuada. Etiam tincidunt mi at tortor vulputate ullamcorper. Proin porta magna ac risus aliquam, vitae posuere nibh feugiat. Aliquam erat volutpat. Aliquam luctus sodales orci.</p>
      <p class="copy">Integer commodo, elit ultrices porta fringilla, nibh nulla convallis dui, nec pellentesque enim erat eu lectus. Integer ultricies magna neque, eget finibus libero molestie vel. Morbi mollis tincidunt lacus nec porttitor. Mauris et purus elit. Donec varius, odio eu commodo tempus, diam lorem hendrerit ligula, a semper nisi nulla a purus.</p>
    </div>
  </section>

  <section class="panel panel--about">
    <div class="about__photo" role="img" aria-label="Faded photo of a sunlit golf course"></div>
    <div class="about__body">
      <h2 class="heading">About us</h2>
      <p class="copy">Lorem ipsum dolor sit amet, consectetur adipiscing elit. Sed dignissim sollicitudin lectus, quis feugiat libero maximus eget. Fusce tincidunt fermentum ligula sed tincidunt. Orci varius natoque penatibus et magnis dis parturient montes, nascetur ridiculus mus. Pellentesque dapibus tellus id iaculis malesuada. Etiam tincidunt mi at tortor vulputate ullamcorper. Proin porta magna ac risus aliquam, vitae posuere nibh feugiat. Aliquam erat volutpat. Aliquam luctus sodales orci.</p>
      <p class="copy">Integer commodo, elit ultrices porta fringilla, nibh nulla convallis dui, nec pellentesque enim erat eu lectus. Integer ultricies magna neque, eget finibus libero molestie vel. Morbi mollis tincidunt lacus nec porttitor. Mauris et purus elit. Donec varius, odio eu commodo tempus, diam lorem hendrerit ligula, a semper nisi nulla a purus. Integer dapibus, eros id gravida eleifend, orci ex pretium erat, sed vulputate turpis mauris suscipit neque. Duis suscipit lacus vel condimentum tincidunt. Vivamus a enim ultrices, varius magna nec, elementum felis. Mauris nec molestie neque. Cras hendrerit congue diam, eget tempor turpis. Phasellus lobortis nisl quam, vitae dictum leo vestibulum a. Vestibulum ac suscipit.</p>
    </div>
    <div class="contact">
      <h2 class="heading">Contact us</h2>
      <dl class="contact__list">
        <dt>Phone</dt><dd>:</dd><dd>403-555-0142</dd>
        <dt>Email</dt><dd>:</dd><dd>info@vantageturf.ca</dd>
        <dt>Website</dt><dd>:</dd><dd>vantageturf.ca</dd>
      </dl>
    </div>
    <div class="brand-mark">
      <span class="brand-mark__name"><span class="brand-mark__dot"></span>Vantage Aerial Turf</span>
    </div>
  </section>

  <section class="panel panel--cover" role="img" aria-label="Close-up photo of a golf ball on a tee over green grass with trees and blue sky behind">
    <div class="cover__seal">
      <p class="cover__name">Vantage<br>Aerial Turf</p>
    </div>
  </section>

</main>
</body>
</html>
```